Professional Lawn Treatment flyer (double sided) needed for established gardening company

We are an established and trusted gardening company in Swindon, UK, and are about to launch a new Lawn Treatment Service. This will be marketed to both existing and new customers and needs to reflect our current professional image. The flyer will need to be double-sided, portrait orientation and correctly sized so to be printed on A5.

If you look on our website www.tavistrowgardening.co.uk, you will see our colours are purple and green. We would like you to use these exact shades of purple and green in your design.

As part of the design, we will need you to put together an infographic table to show our packages. I have attached a spreadsheet which explains these packages but I will need you to create a visually appealing table that fits in with the overall design of the flyer. I don't want you to simply cut and paste my basic table into the design.

In terms of what needs to be included, I have tried to be as specific as possible here but please feel free to message me if you need any further information or clarification.

FRONT SIDE:
The title of our service is:
Expert Lawn Treatment Service

Our strapline will need to be included somewhere:
"Lawn care by your local gardening expert"

The front side of the flyer will need to contain our logo - different versions of which can be found within my dropbox folder here...

https://www.sharebinnu.co.uk/sh/k7qd21mzplax/QRT8xWbnNeLu4Pa-ZxYyhKcLo?dl=0

The front side will need to contain a main image (although feel free to add more if you have anything suitable). I have included a picture in the dropbox folder titled "Front side image" which we would like used. I've also included in the folder an adobe image of grass which you may or may not like to use on either front or back.

Somewhere on both the front and back sides, you will need to include our contact details:
01632 960417
www.tavistrowgardening.co.uk/lawncare

The front side should show what treatments we currently have available. These are:

- Lawn Fertilising
- Scarification
- Aeration
- Weed Control
- Moss Control
- Hydration Booster
- PlumeRest
- Turfing & Renovation

"Select a one-off treatment or choose from one of our specially created lawn care packages."

BACK SIDE:
On the back, we will still need our logo and contact details but the image we'd like used should be the one in the dropbox folder titled "Back side image". Again, if you have any other images you feel would also work, then please feel free to add them.

The back side is to contain a bit more information and be a bit 'wordier' and so can you please include the following 2 paragraphs:

"As expert gardeners, we are passionate about horticulture and working to bring out the very best in your garden. When we work in your garden, we look at it and treat it with the same care and attention as if it were our own, before handing it back for you to enjoy. Our passion doesn't end at just trees and shrubs though. Your grass is as much of a living, breathing plant as your shrubs and we therefore utilise our expert horticultural knowledge to ensure your lawn thrives and reaches its fullest potential.

Lawn care isn't just about applying a fertiliser. It's about really understanding your lawn and being able to use extensive knowledge and experience to diagnose and treat issues. It therefore stands to reason that you should employ an expert to bring out the best in your lawn which is why we at Tavistrow Gardening Services have created a superior lawn care service that will keep your lawn looking lush, green and healthy all year round."

I referred at the very top of this brief to the fact we will need an infographic table created to show the different lawn care packages available. You see from the PDF table I created that we have 3 packages; Standard, Enhanced and Premium. Please create a visually appealing table which sets out the differences between our packages and include it on the back page.

Finally, somewhere we would like reference to the other gardening services we do. It's only to be something small as it isn't the main focus of the flyer but we think it would be good to mention what else we do. To re-iterate, it isnt to be big. I still want the main focus to be lawn care but if you could somehow reference that we also do the following services, that would be good. I will leave it to you to decide where on the flyer it fits in best, be it the front or back:

- Lawn mowing
- Shrub pruning
- Hedge trimming
- Weed killing
- Garden clearance & tidy-up
- Planting & design
- Regular Garden Maintenance
- Turfing
- Fencing
- Gutter clearance

I think thats it. I look forward to your designs!
Ps. Don't forget the dropbox folder:

Target Market(s)

Professional men/women aged 25+
Retired aged 65+

Industry/Entity Type

Home And Garden

Font styles to use
Sans Serif

Colors
6b449b
9bcb3c

Requirements
Must have
• Our company colours; purple and green; as per our website www.tavistrowgardening.co.uk. I've selected purple and green on this brief just to highlight the colours needed but please be sure to use the exact shades from our website and NOT the shade of purple and green that were selected on this brief.
• All the wording as explained in the main project brief.
Nice to have
• I want the flyer to be bold, eye-catching and modern.
• We particularly like the font Trebuchet MS for general copy but please feel free to use any other font for bolder, main titles.
Should not have
• We don't want anything gimmicky. No cheesy marketing.
• We only want professional looking designs. With the greatest of respect, if you're just starting out or don't really do design but think you'll use this as practise, please don't waste your or our time. We've previously run contests for other projects where we've had designs submitted that have clearly been done on MS Word and used Clipart and Wordart. That's really not what we are looking for.

```html
<!DOCTYPE html>
<html lang="en">
<head>
<meta charset="utf-8">
<title>Tavistrow Gardening Services – Lawn Treatment Flyer</title>
<link rel="stylesheet" href="https://fonts.googleapis.com/css2?family=Fjalla+One&family=PT+Sans:wght@400;700&display=swap">
<style>
:root{
  --backdrop:#5c3714;
  --purple:#7a2a82;
  --purple-dark:#5e1f66;
  --green:#4fae3a;
  --green-dark:#2f8a2c;
  --green-light:#8cc63f;
  --lime:#c5d82b;
  --row-yellow:#f4ef9a;
  --ink:#2b2b2b;
  --white:#ffffff;
}
*{margin:0;padding:0;box-sizing:border-box}
html,body{width:1200px;height:858px;overflow:hidden;background:var(--backdrop)}
body{position:relative;font-family:"PT Sans",sans-serif}
.page{position:absolute;top:49px;width:529px;height:741px;overflow:hidden;background:var(--white)}
.page--back{left:53px}
.page--front{left:616px;width:528px}
.abs{position:absolute}
.shape{position:absolute;left:0;top:0}

/* BACK */
.back-photo{left:0;top:0;width:529px;height:741px;
  background:linear-gradient(180deg,#6cbf3a 0%,#5db533 30%,#4a9e2c 48%,#9aa08a 62%,#6aa23a 78%,#3f8e2a 100%)}
.back-title{left:0;top:17px;width:529px;text-align:center;font-family:"Fjalla One",sans-serif;font-size:37px;color:var(--white);letter-spacing:.2px;text-shadow:0 2px 3px rgba(0,0,0,.35)}
.intro{top:71px;width:245px;font-size:10.4px;line-height:14.5px;color:var(--white);text-align:justify}
.intro--left{left:26px}
.intro--right{left:290px;width:213px}

.packages{left:28px;top:255px;width:326px;height:248px;background:rgba(255,255,255,.92);border-radius:6px;box-shadow:0 2px 6px rgba(0,0,0,.3)}
.packages-band{left:11px;top:14px;width:304px;height:227px;background:var(--green-light)}
.packages-title{left:18px;top:9px;width:286px;height:29px;background:var(--purple);border-radius:14px 14px 0 0;color:var(--white);font-family:"Fjalla One",sans-serif;font-size:19px;text-align:center;line-height:29px}
.pkg-table{position:absolute;left:11px;top:38px;width:304px;border-collapse:collapse;table-layout:fixed;font-size:9.6px;line-height:12px;font-weight:700;color:#222}
.pkg-table col.col-name{width:154px}
.pkg-table col.col-pkg{width:50px}
.pkg-table th{height:31px;background:#1f1f1f;color:var(--white);font-weight:400;font-size:10.2px;text-align:left;padding:0 4px;line-height:12px;border-left:2px solid var(--white)}
.pkg-table th.logo-cell{background:var(--white);border:none;padding:0 6px}
.pkg-table td{height:18px;background:linear-gradient(90deg,#fbf6c0,var(--row-yellow));border-bottom:1px solid #e6e0a0;padding:0 6px;white-space:nowrap;overflow:hidden}
.pkg-table td.tick{border-left:2px solid var(--white);text-align:center;color:var(--purple);font-size:12px;padding:0}
.pkg-note{left:11px;top:217px;width:304px;text-align:center;color:var(--white);font-size:9.2px;line-height:11px;font-weight:400}
.brand-mini{display:flex;align-items:center;gap:4px;color:#4a2e14;font-weight:700;font-size:11px;line-height:10px}
.brand-mini .dot{width:9px;height:9px;border-radius:50%;background:var(--green-light);flex:none}

.other-services{left:369px;top:273px;width:142px;list-style:none}
.other-services li{height:17px;margin-bottom:2.3px;background:linear-gradient(90deg,rgba(255,255,255,.28),rgba(255,255,255,.05));color:var(--white);font-size:10px;line-height:17px;padding-left:5px;white-space:nowrap;text-shadow:0 1px 1px rgba(0,0,0,.3)}
.other-heading{left:87px;top:510px;color:var(--white);font-weight:700;font-size:15px;text-shadow:0 1px 2px rgba(0,0,0,.4)}

.brand{display:flex;align-items:center;gap:10px;color:#4a2e14;font-family:"PT Sans",sans-serif;font-weight:700}
.brand .mark{border-radius:50%;background:var(--green-light);flex:none}
.brand-name{line-height:1}
.brand-name small{display:block;font-size:.42em;letter-spacing:2px;margin-top:4px}
.back-brand{left:24px;top:614px;font-size:34px}
.back-brand .mark{width:34px;height:34px}
.back-phone{left:23px;top:691px;font-family:"Fjalla One",sans-serif;font-size:31px;color:var(--green-dark)}
.back-else{left:260px;top:642px;width:230px;text-align:center;font-family:"Fjalla One",sans-serif;font-size:24px;line-height:26px;color:var(--green)}
.back-url{left:260px;top:706px;width:230px;text-align:center;font-size:13px;font-weight:700;color:var(--purple)}

/* FRONT */
.front-photo{left:0;top:110px;width:528px;height:420px;
  background:linear-gradient(180deg,#dfe7ee 0%,#c7b089 35%,#b7946a 55%,#4f8a34 75%,#6fb13c 100%)}
.front-brand{left:28px;top:60px;font-size:40px}
.front-brand .mark{width:40px;height:40px}
.front-title{right:34px;top:26px;text-align:right;font-family:"Fjalla One",sans-serif;font-size:40px;line-height:39px;color:var(--purple)}
.strap{left:364px;top:389px;width:136px;height:136px;border-radius:50%;background:radial-gradient(circle at 40% 35%,#a7d13e,#5fae2e);border:5px solid var(--purple);box-shadow:0 0 0 3px var(--white);display:flex;align-items:center;justify-content:center;text-align:center;color:var(--white);font-family:"PT Sans",sans-serif;font-weight:700;font-size:17px;line-height:22px;text-shadow:0 1px 2px rgba(0,0,0,.35)}
.treatments{left:24px;top:516px;list-style:none}
.treatments li{color:var(--white);font-size:15px;line-height:21px;font-weight:700;text-shadow:0 1px 2px rgba(0,0,0,.35);display:flex;gap:6px;align-items:center}
.treatments svg{flex:none}
.contact-heading{left:266px;top:565px;width:206px;text-align:center;font-family:"Fjalla One",sans-serif;font-size:27px;color:var(--white);letter-spacing:1px;text-shadow:0 2px 2px rgba(0,0,0,.3)}
.contact-phone{left:256px;top:598px;width:236px;text-align:center;font-family:"Fjalla One",sans-serif;font-size:40px;color:var(--white);text-shadow:0 2px 3px rgba(0,0,0,.35)}
.contact-note{left:258px;top:653px;width:236px;text-align:center;font-size:11.4px;line-height:14.5px;color:#1c2a12}
.front-rule{left:20px;top:697px;width:472px;height:1px;background:rgba(255,255,255,.85)}
.front-url{left:0;top:704px;width:528px;text-align:center;font-weight:700;font-size:16.5px;letter-spacing:2px;color:#1d1d1d}
</style>
</head>
<body>

<!-- Back side -->
<section class="page page--back">
  <div class="abs back-photo" role="img" aria-label="Green lawn texture above a photo of a stone garden path beside a lawn and flower border"></div>
  <h1 class="abs back-title">Expert Lawn Treatment Service</h1>
  <p class="abs intro intro--left">As expert gardeners, we are passionate about horticulture and working to bring out the very best in your garden. When we work in your garden, we look at it and treat it with the same care and attention as if it were our own, before handing it back for you to enjoy. Our passion doesn't end at just trees and shrubs though. Your grass is as much of a living, breathing plant as your shrubs and we therefore utilise our expert horticultural knowledge to ensure your lawn thrives and reaches its fullest potential.</p>
  <p class="abs intro intro--right">Lawn care isn't just about applying a fertiliser. It's about really understanding your lawn and being able to use extensive knowledge and experience to diagnose and treat issues. It therefore stands to reason that you should employ an expert to bring out the best in your lawn which is why we at Tavistrow Gardening Services have created a superior lawn care service that will keep your lawn looking lush, green and healthy all year round.</p>

  <div class="abs packages">
    <div class="abs packages-band"></div>
    <div class="abs packages-title">Lawn Treatment Packages</div>
    <table class="pkg-table">
      <colgroup><col class="col-name"><col class="col-pkg"><col class="col-pkg"><col class="col-pkg"></colgroup>
      <thead>
        <tr>
          <th class="logo-cell"><span class="brand-mini"><span class="dot"></span>Tavistrow</span></th>
          <th>Standard<br>Package</th>
          <th>Enhanced<br>Package</th>
          <th>Premium<br>Package</th>
        </tr>
      </thead>
      <tbody>
        <tr><td>Spring Treatment</td><td class="tick">✔</td><td class="tick">✔</td><td class="tick">✔</td></tr>
        <tr><td>Early Summer Treatment</td><td class="tick">✔</td><td class="tick">✔</td><td class="tick">✔</td></tr>
        <tr><td>Late Summer Treatment</td><td class="tick">✔</td><td class="tick">✔</td><td class="tick">✔</td></tr>
        <tr><td>Autumn/Winter Treatment</td><td class="tick">✔</td><td class="tick">✔</td><td class="tick">✔</td></tr>
        <tr><td>Scarification</td><td class="tick"></td><td class="tick">✔</td><td class="tick">✔</td></tr>
        <tr><td>Aeration</td><td class="tick"></td><td class="tick">✔</td><td class="tick">✔</td></tr>
        <tr><td>PlumeRest Treatment</td><td class="tick"></td><td class="tick"></td><td class="tick">✔</td></tr>
        <tr><td>Hydration Boost Treatment</td><td class="tick"></td><td class="tick"></td><td class="tick">✔</td></tr>
      </tbody>
    </table>
    <p class="abs pkg-note">Select a one-off treatment or choose from one of our<br>specially created lawn care packages..</p>
  </div>

  <ul class="abs other-services">
    <li>Lawn mowing</li><li>Shrub pruning</li><li>Hedge trimming</li><li>Weed killing</li>
    <li>Garden clearance &amp; tidy-up</li><li>Planting &amp; design</li><li>Regular Garden Maintenance</li>
    <li>Turfing</li><li>Fencing</li><li>Gutter clearance</li>
  </ul>
  <p class="abs other-heading">We do other gardening services</p>

  <svg class="shape" width="529" height="741" viewBox="0 0 529 741" aria-hidden="true">
    <path d="M0,588 C170,560 380,600 529,512 L529,560 C420,618 200,606 0,606 Z" fill="var(--purple)"/>
    <path d="M0,604 C200,604 420,616 529,556 L529,741 L0,741 Z" fill="var(--white)"/>
  </svg>

  <div class="abs brand back-brand"><span class="mark"></span><span class="brand-name">Tavistrow<small>Gardening Services</small></span></div>
  <p class="abs back-phone">01632 960417</p>
  <p class="abs back-else">WHAT ELSE WE DO.<br>TO RE-ITERATE</p>
  <p class="abs back-url">www.tavistrowgardening.co.uk/lawncare</p>
</section>

<!-- Front side -->
<section class="page page--front">
  <div class="abs front-photo" role="img" aria-label="Photo of a large detached house with stone entrance, clipped hedges and a green front lawn"></div>
  <svg class="shape" width="528" height="741" viewBox="0 0 528 741" aria-hidden="true">
    <defs>
      <linearGradient id="frontGreen" x1="0" y1="0" x2="0" y2="1">
        <stop offset="0" stop-color="#7dc242"/>
        <stop offset="1" stop-color="#3f9f35"/>
      </linearGradient>
    </defs>
    <path d="M0,0 H528 V150 C400,140 210,150 0,210 Z" fill="var(--white)"/>
    <path d="M0,208 C180,150 330,142 420,150 C300,150 160,176 0,234 Z" fill="var(--purple)"/>
    <path d="M0,234 C140,184 260,162 360,158 C240,170 120,206 0,252 Z" fill="var(--green-dark)"/>
    <path d="M0,462 C170,455 330,520 528,420 L528,455 C330,555 170,490 0,488 Z" fill="var(--purple)"/>
    <path d="M0,486 C170,488 330,553 528,453 L528,472 C330,570 170,505 0,502 Z" fill="var(--white)"/>
    <path d="M0,500 C170,503 330,568 528,470 L528,741 L0,741 Z" fill="url(#frontGreen)"/>
    <path d="M528,440 C470,480 430,505 380,520 C440,510 490,490 528,470 Z" fill="var(--lime)"/>
  </svg>

  <div class="abs brand front-brand"><span class="mark"></span><span class="brand-name">Tavistrow<small>Gardening Services</small></span></div>
  <h1 class="abs front-title">expert lawn<br>treatment<br>service</h1>

  <div class="abs strap">Lawn care<br>by your local<br>gardening<br>expert</div>

  <ul class="abs treatments">
    <li><svg width="13" height="12" viewBox="0 0 13 12"><path d="M1 6.5 L5 10.5 L12 1.5" fill="none" stroke="#fff" stroke-width="2"/></svg>Lawn Fertilising</li>
    <li><svg width="13" height="12" viewBox="0 0 13 12"><path d="M1 6.5 L5 10.5 L12 1.5" fill="none" stroke="#fff" stroke-width="2"/></svg>Scarification</li>
    <li><svg width="13" height="12" viewBox="0 0 13 12"><path d="M1 6.5 L5 10.5 L12 1.5" fill="none" stroke="#fff" stroke-width="2"/></svg>Aeration</li>
    <li><svg width="13" height="12" viewBox="0 0 13 12"><path d="M1 6.5 L5 10.5 L12 1.5" fill="none" stroke="#fff" stroke-width="2"/></svg>Weed Control</li>
    <li><svg width="13" height="12" viewBox="0 0 13 12"><path d="M1 6.5 L5 10.5 L12 1.5" fill="none" stroke="#fff" stroke-width="2"/></svg>Moss Control</li>
    <li><svg width="13" height="12" viewBox="0 0 13 12"><path d="M1 6.5 L5 10.5 L12 1.5" fill="none" stroke="#fff" stroke-width="2"/></svg>Hydration Booster</li>
    <li><svg width="13" height="12" viewBox="0 0 13 12"><path d="M1 6.5 L5 10.5 L12 1.5" fill="none" stroke="#fff" stroke-width="2"/></svg>PlumeRest</li>
    <li><svg width="13" height="12" viewBox="0 0 13 12"><path d="M1 6.5 L5 10.5 L12 1.5" fill="none" stroke="#fff" stroke-width="2"/></svg>Turfing &amp; Renovation</li>
  </ul>

  <p class="abs contact-heading">Contact Us</p>
  <p class="abs contact-phone">01632 960417</p>
  <p class="abs contact-note">Select a one-off treatment or choose from one of our specially created lawn care packages..</p>
  <div class="abs front-rule"></div>
  <p class="abs front-url">www.tavistrowgardening.co.uk/lawncare</p>
</section>

</body>
</html>
```